■依頼の目的/概要
ビジネス本の表紙デザインをお願いします。

■本の内容
・起業初期の起業家、または副業で月収入10万円UPしたい方向けの、
77のWEBのアドバイス(テクニック)をまとめた本です。

■デザイン要望
どちらかというと、30~50代女性起業家向けです。
女性のイラストが入ると嬉しいです。

その他何かご不明な点がございましたら、お気軽にご質問下さい。
よろしくお願いいたします。

■プレセントの記載をお願いします。
①何が足りないかすぐ分かる!
WEBチェックシート

②1年で1万人フォロワーを達成した
Plumoraフォロワー増やしのコツ

③最短で成功へ向かう無料コンサル

女性らしい優しい雰囲気で、誰からも愛されるデザインと感じました。

この度はご応募頂き、誠にありがとうございました!

どのデザインも素敵で、本当に迷いました。
修正していただいた方には、親切に対応して頂き心より感謝しております。

皆様の益々のご活躍を祈念しております。
今回は本当に有難うございました。

```html
<!DOCTYPE html>
<html lang="ja">
<head>
<meta charset="utf-8">
<title>知っておくべきWEBテクニック77のポイント</title>
<link rel="stylesheet" href="https://fonts.googleapis.com/css2?family=Noto+Sans+JP:wght@500;700;900&family=Noto+Serif+JP:wght@700;900&display=swap">
<style>
  :root{
    --pink:#e8457a;
    --pink-soft:#fbe3ea;
    --pink-pale:#fdf1f4;
    --purple:#8a3a9c;
    --plum:#5a2a6a;
    --ink:#3a2a36;
    --paper:#ffffff;
  }
  *{margin:0;padding:0;box-sizing:border-box}
  html,body{width:750px;height:1200px;overflow:hidden;background:var(--paper)}
  .cover{position:relative;width:750px;height:1200px;overflow:hidden;
    background:linear-gradient(160deg,var(--pink-pale) 0%,var(--paper) 30%,var(--paper) 75%,var(--pink-pale) 100%);
    font-family:"Noto Sans JP",sans-serif;color:var(--ink)}
  .tagline{position:absolute;top:28px;left:0;width:100%;display:flex;justify-content:center;align-items:flex-end;gap:10px;
    font-weight:700;font-size:30px;color:var(--ink)}
  .tagline .amount{border:3px solid var(--pink);border-radius:10px;padding:0 14px;color:var(--pink);font-weight:900;font-size:40px;line-height:1.3;background:var(--paper)}
  .lead{position:absolute;top:98px;left:0;width:100%;text-align:center;font-family:"Noto Serif JP",serif;font-weight:900;font-size:70px;letter-spacing:4px;color:var(--ink)}
  .title-web{position:absolute;top:200px;left:0;width:100%;text-align:center;font-family:"Noto Serif JP",serif;font-weight:900;font-size:230px;line-height:1;letter-spacing:-4px;
    background:linear-gradient(90deg,var(--purple),var(--pink));-webkit-background-clip:text;background-clip:text;color:transparent}
  .title-tech{position:absolute;top:418px;left:0;width:100%;text-align:center;font-weight:900;font-size:122px;line-height:1.1;color:var(--pink);letter-spacing:-2px}
  .title-count{position:absolute;top:555px;right:78px;font-weight:900;line-height:1;color:var(--pink)}
  .title-count .num{font-size:140px;letter-spacing:-6px}
  .title-count .no{font-size:100px;color:var(--purple)}
  .title-points{position:absolute;top:695px;right:40px;font-weight:900;font-size:84px;color:var(--plum);letter-spacing:2px}
  .author{position:absolute;top:808px;right:55px;font-family:"Noto Serif JP",serif;font-weight:700;font-size:34px;color:var(--ink)}
  .author small{font-size:24px;margin-left:8px}
  .illustration{position:absolute;top:600px;left:40px;width:370px;height:250px;border-radius:40% 50% 20% 30%;
    background:radial-gradient(circle at 45% 40%,#f4b9a4 0%,#f6d2cf 45%,rgba(253,241,244,0) 75%)}
  .gifts{position:absolute;top:882px;left:22px;width:706px;height:300px;border:3px solid var(--pink);border-radius:24px}
  .gifts-label{position:absolute;top:-26px;left:50%;transform:translateX(-50%);background:var(--paper);padding:0 22px;
    font-weight:900;font-size:38px;color:var(--pink);white-space:nowrap;font-style:italic}
  .gift-list{position:absolute;top:38px;left:0;width:100%;display:flex;justify-content:space-around}
  .gift{width:224px;height:224px;border-radius:50%;background:var(--paper);border:3px solid var(--pink-soft);
    box-shadow:0 0 0 8px var(--pink-soft);display:flex;flex-direction:column;align-items:center;justify-content:center;text-align:center;line-height:1.25}
  .gift-no{font-weight:900;font-size:28px;color:var(--ink);margin-bottom:6px}
  .gift-note{font-weight:700;font-size:20px;color:var(--ink)}
  .gift-name{font-family:"Noto Serif JP",serif;font-weight:900;font-size:29px;color:var(--pink)}
  .gift-name.sm{font-size:21px}
</style>
</head>
<body>
<main class="cover">
  <p class="tagline"><span>毎月収入</span><span class="amount">10万円UP</span><span>したいあなたに贈る!</span></p>
  <h1>
    <span class="lead">知っておくべき</span>
    <span class="title-web">WEB</span>
    <span class="title-tech">テクニック</span>
    <span class="title-count"><span class="num">77</span><span class="no">の</span></span>
    <span class="title-points">ポイント</span>
  </h1>
  <div class="illustration" role="img" aria-label="ノートパソコンの前でコーヒーカップを持つ女性のイラストと、周りに浮かぶSNSのアイコン"></div>
  <p class="author">花森 ゆりこ<small>著</small></p>

  <section class="gifts">
    <h2 class="gifts-label">3つの読者プレゼント</h2>
    <div class="gift-list">
      <div class="gift">
        <span class="gift-no">特典1</span>
        <span class="gift-note">何が足りないか<br>すぐ分かる!</span>
        <span class="gift-name">WEBチェック<br>シート</span>
      </div>
      <div class="gift">
        <span class="gift-no">特典2</span>
        <span class="gift-note">1年で1万人<br>フォロワーを達成した</span>
        <span class="gift-name sm">Plumoraフォロワー<br>増やしのコツ</span>
      </div>
      <div class="gift">
        <span class="gift-no">特典3</span>
        <span class="gift-note">最短で成功へ向かう</span>
        <span class="gift-name">無料<br>コンサル</span>
      </div>
    </div>
  </section>
</main>
</body>
</html>
```